Cambodia 501c3 flyer design

I need a flyer to build interest and awareness for a school year kick off event in October for our charity school in rural Cambodia. I have text and photos available and just need help getting a professional look and feel. (Other projects may follow, including logo and web redesign.)

Founded in 2004 by Lars Trulsen, The Riverside Learning House at Prek Sala is a 501(c)(3) organization dedicated to breaking the cycle of poverty of some of Cambodia's poorest children by providing a rigorous core K-9 education that emphasizes English proficiency.

"The board of directors of The Riverside Learning House at Prek Sala invites you to our annual visit to Prek Sala, Cambodia to help launch the new school year. The trip is open to everyone-you do not need to be a current donor to attend.

If you have been interested in visiting an educational project that works for hundreds of the poorest children in Cambodia, here is your chance. This school is a lifeline for these children and their families, providing education, transportation, uniforms, and two meals a day."
Updates

Hi everyone! I am really impressed by these designs and there are some really promising directions. One thing I would like to see is revisions with more white space, with the blues and yellows as more accents. Any sort of conservative sans serif font is fine.

Also, in general I will need the final in some kind of editable format where I can make basic text updates. I can do this with either AI or Word. 

The use of the kids' photos is great! I will issue a preliminary cut in the next few days. Thank you all again very much for your work on the behalf of the school and children of Cambodia!

Reason: Hi all, I am going to extend the deadline by 7 days so that I have a chance to review the comps with the other board members. That meeting takes place on 21 April so I should be able to proceed shortly thereafter.

Target Market(s)

For this piece, current donors and prospective donors

Industry/Entity Type

Education

Requirements
Nice to have
• Use any elements from www.riversidelearnhouse.org as you see fit. There are lots of photos of the students that might be helpful. There are also more photos of the school at my Flickr account at
http://www.photoshelfhub.com/photos/58172046@K07/page4/

```html
<!DOCTYPE html>
<html lang="en">
<head>
<meta charset="utf-8">
<title>School Year Kick-Off Visit – The Details</title>
<link rel="stylesheet" href="https://fonts.googleapis.com/css2?family=Source+Sans+3:wght@400;600;700;800&display=swap">
<style>
  :root {
    --navy: #2b3990;
    --navy-deep: #262f7e;
    --navy-row: #3a4aa6;
    --yellow: #fff200;
    --green-label: #1f7a3a;
    --green: #8dc63f;
    --blue-label: #1b4f9c;
    --blue: #29a9e0;
    --red-label: #8c1a1f;
    --red: #c1272d;
    --ink: #1c1c1c;
    --white: #ffffff;
  }
  * { margin: 0; padding: 0; box-sizing: border-box; }
  html, body { width: 927px; height: 1200px; overflow: hidden; background: var(--white); }
  body { font-family: "Source Sans 3", "Myriad Pro", Arial, sans-serif; }

  .flyer { position: relative; width: 927px; height: 1200px; background: var(--navy); overflow: hidden; }

  .photo { position: absolute; }
  .photo-classroom { left: 0; top: 0; width: 292px; height: 224px; background: linear-gradient(160deg, #c9b79c, #8a6f52 60%, #e8e4dc); }
  .photo-dance { left: 295px; top: 0; width: 308px; height: 224px; background: linear-gradient(170deg, #6f8a5a, #c8a050 55%, #a0462c); }
  .photo-kitchen { left: 606px; top: 0; width: 321px; height: 224px; background: linear-gradient(200deg, #d9d4c8, #6f6a5e 55%, #3b3832); }
  .photo-students-wave { left: 0; top: 830px; width: 310px; height: 230px; background: linear-gradient(170deg, #9bbf7c, #dfe3e6 55%, #5b6b7d); }
  .photo-students-group { left: 314px; top: 830px; width: 300px; height: 230px; background: linear-gradient(180deg, #cfd6dc, #e9ecef 45%, #4a5a78); }
  .photo-guests { left: 617px; top: 830px; width: 310px; height: 230px; background: linear-gradient(180deg, #2f6a3a, #c8b06a 60%, #d8c58a); }

  .details-title {
    position: absolute; left: 0; top: 224px; width: 61px; height: 329px;
    background: var(--navy-deep);
    display: flex; align-items: center; justify-content: center;
  }
  .details-title span {
    writing-mode: vertical-rl; transform: rotate(180deg); white-space: nowrap;
    color: var(--yellow); font-weight: 600; font-size: 44px; letter-spacing: 4px; line-height: 1;
  }

  .row { position: absolute; left: 61px; right: 0; display: flex; }
  .row-label {
    width: 40px; display: flex; align-items: center; justify-content: center; color: var(--white);
  }
  .row-label > span {
    writing-mode: vertical-rl; transform: rotate(180deg); white-space: nowrap; line-height: 1.05; text-align: left;
  }
  .row-label .day { display: block; font-weight: 800; font-size: 22px; letter-spacing: 0.5px; }
  .row-label .date { font-size: 14px; font-weight: 400; }
  .row-body { flex: 1; display: flex; align-items: center; padding: 0 14px 0 22px; font-size: 13px; line-height: 1.45; color: var(--ink); }

  .row-monday { top: 227px; height: 106px; }
  .row-monday .row-label { background: var(--green-label); }
  .row-monday .row-body { background: var(--green); }

  .row-tuesday { top: 336px; height: 159px; }
  .row-tuesday .row-label { background: var(--blue-label); }
  .row-tuesday .row-body { background: var(--blue); text-align: justify; }
  .hotel-gap { display: inline-block; width: 110px; }

  .row-cost { top: 498px; height: 55px; }
  .row-cost .row-label { background: var(--red-label); }
  .row-cost .row-label .cost-line { display: block; font-weight: 800; font-size: 14px; letter-spacing: 0.5px; line-height: 1.05; }
  .row-cost .row-body { background: var(--red); color: var(--white); font-weight: 600; font-size: 15px; line-height: 1.35; padding-left: 14px; }

  .more-info { position: absolute; left: 14px; right: 14px; top: 566px; color: var(--white); font-size: 13.5px; line-height: 1.4; }
  .more-info p + p { margin-top: 4px; }

  .contacts { position: absolute; left: 0; right: 0; top: 662px; }
  .contact {
    display: grid; grid-template-columns: 362px 260px 1fr; align-items: center;
    height: 53px; margin-bottom: 3px; padding-left: 14px;
    background: var(--navy-row); color: var(--white);
  }
  .contact-name { font-size: 21px; font-weight: 700; line-height: 1; }
  .contact-role { font-size: 14px; line-height: 1.2; }
  .contact-phone, .contact-email { font-size: 18px; }

  .about { position: absolute; left: 14px; right: 14px; top: 1072px; color: var(--white); font-size: 13.5px; line-height: 1.38; text-align: justify; }
</style>
</head>
<body>
<main class="flyer">
  <div class="photo photo-classroom" role="img" aria-label="Photo of students in white uniforms seated at classroom desks"></div>
  <div class="photo photo-dance" role="img" aria-label="Photo of students performing a traditional Cambodian dance in costume"></div>
  <div class="photo photo-kitchen" role="img" aria-label="Photo of a cook stirring a large wok in the school kitchen"></div>

  <div class="details-title"><span>THE DETAILS</span></div>

  <section class="row row-monday">
    <div class="row-label"><span><b class="day">MONDAY</b><span class="date">September 30</span></span></div>
    <div class="row-body"><p>You should plan on arriving in Siem Reap either from Bangkok or Phnom Penh. There will be a cocktail party and mixer for visitors, donors and guests that evening. The location and time will be announced on the website.</p></div>
  </section>

  <section class="row row-tuesday">
    <div class="row-label"><span><b class="day">TUESDAY</b><span class="date">October 1</span></span></div>
    <div class="row-body"><p>We will meet in the lobby of the <span class="hotel-gap"></span> Hotel at 8:30 a.m. to board private, air conditioned buses to the campus. The trip takes about 90 minutes. We will open as the students sing the Cambodian national anthem, and the students will put on a brief performance of local dances. All guests will have special ‘VIP’ seating and will listen to brief talks by Lars Trulsen, the founder, as well as the local provincial governor. The school will provide lunch, and there will be plenty of time for a tour of the campus as well as, most importantly, to interact with the boys and girls, many of whom are very eager to practice their English. We will return to town around 3:00 p.m. and will meet for dinner on Siem Reap’s famous ‘Pub Street’.</p></div>
  </section>

  <section class="row row-cost">
    <div class="row-label"><span><b class="cost-line">THE</b><b class="cost-line">COST</b></span></div>
    <div class="row-body"><p>You are responsible for your own travel arrangements, but there is no cost to attend the event. Lunch and transportation to and from the school is provided by our donors.</p></div>
  </section>

  <section class="more-info">
    <p>For more details, visit www.riversidelearnhouse.org/2013trip for travel tips and other suggestions about what to see and do in Cambodia.</p>
    <p>If you have questions about this once in a lifetime opportunity, please contact one of the board members below. We are happy to help with specific travel tips and recommendations.</p>
  </section>

  <section class="contacts">
    <div class="contact">
      <div><div class="contact-name">Lars Trulsen</div><div class="contact-role">Founder And President</div></div>
      <div class="contact-phone">000-000-0000</div>
      <div class="contact-email">email@email.com</div>
    </div>
    <div class="contact">
      <div><div class="contact-name">Peter Lindqvist</div><div class="contact-role">Secretary And Director</div></div>
      <div class="contact-phone">000-000-0000</div>
      <div class="contact-email">email@email.com</div>
    </div>
    <div class="contact">
      <div><div class="contact-name">Dana Whitford</div><div class="contact-role">Treasurer And Director</div></div>
      <div class="contact-phone">555-214-0398</div>
      <div class="contact-email">dana@riversidelearnhouse.org</div>
    </div>
  </section>

  <div class="photo photo-students-wave" role="img" aria-label="Photo of smiling students raising their hands outdoors"></div>
  <div class="photo photo-students-group" role="img" aria-label="Photo of a large group of students posing with a visitor in front of the school"></div>
  <div class="photo photo-guests" role="img" aria-label="Photo of guests seated at the annual educational ceremony"></div>

  <p class="about">Founded in 2004 by Lars Trulsen, the Riverside Learning House at Prek Sala is a 501(c)(3) organization dedicated to breaking the cycle of poverty of some of Cambodia’s poorest children by providing a rigorous core K-9 education that emphasizes English proficiency. All donations are 100% passed through for the needs of the school. All administrative costs are paid personally by the board, and financial statements are always available on request.</p>
</main>
</body>
</html>
```